Bref créative
BrightPath Fuel
Eye Catching Card & Letterhead Design
Professional
Marcus Torres
CEO
4183 HAWTHORNE AVE
SUITE 310
SARASOTA FL 34519
mtorres@brightpathfuel.example
www.brightpathfuel.example
use the WELL portion of the logo and list the twitter site (@brightpathfuel)

```html
<!DOCTYPE html>
<html lang="en">
<head>
<meta charset="utf-8">
<title>BrightPath Fuel – Business Cards</title>
<link rel="stylesheet" href="https://fonts.googleapis.com/css2?family=Open+Sans:wght@400;600;700&display=swap">
<style>
  :root {
    --backdrop: #e4ded6;
    --card-white-top: #ffffff;
    --card-white-bottom: #e9e9ea;
    --brand-green: #8dbb2a;
    --green-light: #b8d53a;
    --green-dark: #7aa82b;
    --ink: #1d1d1b;
    --ink-soft: #3a3a3a;
    --white: #ffffff;
  }
  * { margin: 0; padding: 0; box-sizing: border-box; }
  html, body { width: 1200px; height: 763px; overflow: hidden; }
  body {
    position: relative;
    background: var(--backdrop);
    font-family: "Open Sans", Arial, sans-serif;
    color: var(--ink);
  }
  .card {
    position: absolute;
    border-radius: 14px;
    box-shadow: 0 4px 14px rgba(0,0,0,0.18);
    display: flex;
    flex-direction: column;
    align-items: center;
  }
  .card--white {
    background: linear-gradient(180deg, var(--card-white-top) 0%, var(--card-white-bottom) 100%);
  }
  .card--green {
    background: linear-gradient(100deg, var(--green-light) 0%, var(--brand-green) 55%, var(--green-dark) 100%);
  }
  .card--contact { left: 91px; top: 132px; width: 456px; height: 367px; z-index: 2; padding-top: 52px; }
  .card--back-green { left: 631px; top: 72px; width: 497px; height: 288px; z-index: 1; justify-content: center; }
  .card--back-white { left: 396px; top: 401px; width: 540px; height: 314px; z-index: 1; justify-content: center; }

  .brand { display: flex; flex-direction: column; align-items: center; gap: 8px; }
  .brand__dot { width: 30px; height: 30px; border-radius: 50%; background: var(--brand-green); }
  .brand--on-green .brand__dot { background: var(--white); }
  .brand__name {
    font-weight: 600;
    letter-spacing: -0.5px;
    line-height: 1;
    color: var(--ink);
    white-space: nowrap;
  }
  .brand--on-green .brand__name { color: var(--white); }
  .card--contact .brand__name { font-size: 42px; }
  .card--back-green .brand__name { font-size: 48px; }
  .card--back-white .brand__name { font-size: 52px; }

  .contact { margin-top: 34px; text-align: center; }
  .contact__person { font-size: 19px; margin-bottom: 16px; }
  .contact__name { color: var(--brand-green); font-weight: 700; }
  .contact__divider { color: var(--ink-soft); margin: 0 6px; }
  .contact__title { font-size: 14px; color: var(--ink-soft); }
  .contact__line { font-size: 13.5px; line-height: 1.45; color: var(--ink); }
</style>
</head>
<body>
  <section class="card card--white card--contact">
    <div class="brand">
      <span class="brand__dot"></span>
      <span class="brand__name">BrightPath Fuel</span>
    </div>
    <div class="contact">
      <p class="contact__person"><span class="contact__name">Marcus Torres</span><span class="contact__divider">|</span><span class="contact__title">CEO</span></p>
      <p class="contact__line">4183 HAWTHORNE AVE, Suite 310, Sarasota FL 34519</p>
      <p class="contact__line">Cell: 407.555.0142 &nbsp;|&nbsp; Email: mtorres@brightpathfuel.example</p>
      <p class="contact__line">www.brightpathfuel.example</p>
    </div>
  </section>

  <section class="card card--green card--back-green">
    <div class="brand brand--on-green">
      <span class="brand__dot"></span>
      <span class="brand__name">BrightPath Fuel</span>
    </div>
  </section>

  <section class="card card--white card--back-white">
    <div class="brand">
      <span class="brand__dot"></span>
      <span class="brand__name">BrightPath Fuel</span>
    </div>
  </section>
</body>
</html>
```